Infill Flyer

We would like a flyer designed.

8.5 inches x 11 inches

Clean, fresh, professional, scientific look

I realize that a few of my photos are not high resolution, but I will be using this for electronic transmission for now. Thanks!

Industry/Entity Type

Electronic

Font styles to use
Sans Serif

```html
<!DOCTYPE html>
<html lang="en">
<head>
<meta charset="UTF-8">
<title>Infill Options Flyer</title>
<link rel="stylesheet" href="https://fonts.googleapis.com/css2?family=Roboto:wght@300;400&display=swap">
<style>
  :root {
    --accent: #f07a2c;
    --rule: #f3b58a;
    --ink: #2b2b2b;
    --paper: #ffffff;
    --turf-dark: #2f4a25;
    --turf-mid: #556b3a;
    --grass-green: #3f8f3a;
    --grass-brown: #8a6a4c;
  }
  html, body {
    margin: 0;
    padding: 0;
    overflow: hidden;
    background: var(--paper);
  }
  .flyer {
    position: relative;
    width: 928px;
    height: 1200px;
    background: var(--paper);
    font-family: "Roboto", Arial, sans-serif;
    color: var(--ink);
    overflow: hidden;
  }
  .section-rule {
    position: absolute;
    left: 0;
    width: 262px;
    height: 3px;
    background: linear-gradient(to right, var(--rule), rgba(243,181,138,0.15));
  }
  .section-title {
    position: absolute;
    left: 39px;
    margin: 0;
    font-weight: 300;
    font-size: 34px;
    line-height: 1;
    color: var(--accent);
  }
  .section-photo {
    position: absolute;
    left: 260px;
    width: 450px;
    height: 72px;
  }
  .photo-infill {
    background: radial-gradient(circle at 30% 40%, var(--turf-mid), var(--turf-dark) 70%);
  }
  .photo-grass {
    background: linear-gradient(100deg, var(--grass-green) 0%, #5aa84a 35%, var(--grass-brown) 60%, var(--grass-green) 100%);
  }
  .body-copy {
    position: absolute;
    left: 39px;
    width: 820px;
    margin: 0;
    font-weight: 300;
    font-size: 20.5px;
    line-height: 25px;
  }
  .summary-title {
    position: absolute;
    left: 39px;
    top: 644px;
    margin: 0;
    font-weight: 300;
    font-size: 34px;
    color: var(--accent);
  }
</style>
</head>
<body>
<main class="flyer">
  <div class="section-rule" style="top:97px"></div>
  <h2 class="section-title" style="top:118px">TerraCoat</h2>
  <div class="section-photo photo-infill" style="top:95px" role="img" aria-label="Close-up of coated sand infill granules among turf fibres"></div>
  <p class="body-copy" style="top:187px">This is acrylic-coated sand and is not a replacement for rubber. Drawbacks include the risk of chipping of the coating, use of dyes, and lack of testing. Moreover, acrylic-coated sand does not absorb shock and requires the use of a pad.<br>Cost estimate: $0.22 per pound.</p>

  <div class="section-rule" style="top:379px"></div>
  <h2 class="section-title" style="top:400px">TPE</h2>
  <div class="section-photo photo-grass" style="top:379px" role="img" aria-label="Close-up of green turf blades with organic infill"></div>
  <p class="body-copy" style="top:470px">Organics—Various organic options exist, including coconut husks and cork. Organic infill has seen some success in the cool, damp regions of Europe. However, these organic options risk decomposition and breakdown. Organic infills can float and migrate away, and most need to be regularly watered in order mimic the European climate.</p>

  <h2 class="summary-title">So what’s the big picture?</h2>
  <p class="body-copy" style="top:712px">The fact is that the so-called “alternative” infills are not risk-free, and they have not been subjected to the same level of scrutiny that crumb rubber has.<br>Of all the other options, our favorite is Vantor Grind because of the strength of Vantor’s QC processes and the environmentally friendly recycling process.</p>
</main>
</body>
</html>
```